Podiatry clinic requires a modern revamp and editing of existing website.

I would like a fresh new look and updated information for my current business website. An easy to navigate site with prominent address and phone number for call to action. We are a podiatry clinic that focuses on general and sports podiatry.
I would like 4 pages; including Home page, About Us, Services & Contact.
www.brambleridgefootcare.com

Target Market(s)

Active working professionals.

Industry/Entity Type

Medical

Coding

Coded - Design and coding required

Number of Pages Required

4 page

Font styles to use
Sans Serif

Colors
6b449b

Requirements
Must have
• A modern look with logo and active images; clean and uncluttered. Visible phone number and address for call to action.
• 4 pages - Home, About Us, Services, Contact.
• Home page - update address & service logos.
• About Us - update of personal information.
• Services - Revamp of existing page.
• Contact page to include Google map, email & phone number.
Nice to have
• Ability to add content easily; eg. a blog or adding video onto Home page.
• Link to Facebook page.

```html
<!DOCTYPE html>
<html lang="en">
<head>
<meta charset="utf-8">
<title>Bramble Ridge Foot Care</title>
<link rel="stylesheet" href="https://fonts.googleapis.com/css2?family=Open+Sans:wght@300;400;500;600;700&family=Questrial&display=swap">
<style>
  :root {
    --purple: #7b5cb8;
    --purple-band: #7452a3;
    --purple-nav: #6b449b;
    --ink: #222;
    --body-text: #7a7a7a;
    --nav-text: #555;
    --footer-bg: #363636;
    --footer-muted: #9a9a9a;
    --hero-top: #c3cfd7;
    --hero-bottom: #d5cdc1;
    --white: #fff;
  }
  * { box-sizing: border-box; margin: 0; padding: 0; }
  html, body { width: 1013px; height: 1200px; overflow: hidden; background: var(--white); }
  body { position: relative; font-family: "Open Sans", sans-serif; color: var(--ink); }

  .site-header { position: absolute; top: 0; left: 0; width: 1013px; height: 47px; background: var(--white); border-bottom: 1px solid #e6e6e6; }
  .brand { position: absolute; left: 53px; top: 14px; font-size: 14.5px; font-weight: 500; letter-spacing: 0.1px; color: var(--ink); }
  .main-nav { position: absolute; top: 19px; left: 0; width: 100%; }
  .main-nav a { position: absolute; font-size: 7px; letter-spacing: 0.4px; text-transform: uppercase; color: var(--nav-text); text-decoration: none; white-space: nowrap; }
  .main-nav a.is-active { color: var(--purple-nav); font-weight: 600; }

  .hero { position: absolute; top: 47px; left: 0; width: 1013px; height: 523px;
    background: linear-gradient(180deg, var(--hero-top) 0%, var(--hero-bottom) 100%); }
  .hero-copy { position: absolute; left: 0; width: 100%; text-align: center; color: var(--white); font-family: "Questrial", sans-serif; }
  .hero-address { top: 193px; font-size: 22px; letter-spacing: 1.5px; }
  .hero-phone { top: 237px; font-size: 17px; letter-spacing: 0.3px; }
  .hero-email { top: 262px; font-size: 17px; }
  .btn { position: absolute; height: 29px; display: flex; align-items: center; justify-content: center; font-size: 7.5px; font-weight: 700; color: var(--white); text-transform: uppercase; letter-spacing: 0.2px; }
  .btn-solid { background: var(--purple); }
  .btn-outline { border: 1px solid var(--purple); }
  .hero .btn-solid { left: 396px; top: 318px; width: 105px; }
  .hero .btn-outline { left: 512px; top: 318px; width: 105px; border-color: #8b76b8; }
  .slider-arrow { position: absolute; top: 247px; width: 29px; height: 29px; background: rgba(90,90,90,0.65); display: flex; align-items: center; justify-content: center; }
  .slider-arrow.prev { left: 26px; }
  .slider-arrow.next { left: 958px; }
  .slider-dots { position: absolute; top: 499px; left: 478px; display: flex; gap: 9px; align-items: center; }
  .slider-dots span { width: 7px; height: 7px; border-radius: 50%; background: rgba(255,255,255,0.6); }
  .slider-dots span.is-current { width: 9px; height: 9px; background: var(--white); }

  .intro { position: absolute; top: 638px; left: 186px; width: 640px; text-align: center; font-size: 10.7px; line-height: 16px; color: var(--body-text); font-weight: 400; }
  .intro p { margin-bottom: 15.5px; }
  .cta-bar { position: absolute; height: 19px; background: var(--purple); color: var(--white); font-size: 10.5px; font-weight: 600; display: flex; align-items: center; justify-content: center; white-space: nowrap; }
  .cta-call { left: 344px; top: 779px; width: 326px; }
  .cta-mail { left: 376px; top: 810px; width: 262px; }

  .promo-band { position: absolute; top: 902px; left: 0; width: 1013px; height: 95px; background: var(--purple-band); color: var(--white); }
  .promo-title { position: absolute; left: 196px; top: 26px; font-size: 15.8px; font-weight: 300; }
  .promo-text { position: absolute; left: 198px; top: 50px; width: 380px; font-size: 9px; line-height: 10.5px; font-weight: 300; }
  .promo-band .btn-outline { left: 672px; top: 33px; width: 143px; border-color: var(--white); }

  .site-footer { position: absolute; top: 997px; left: 0; width: 1013px; height: 203px; background: var(--footer-bg); color: var(--white); }
  .footer-brand { position: absolute; top: 28px; width: 100%; text-align: center; font-size: 14px; font-weight: 600; }
  .footer-col { position: absolute; top: 89px; }
  .footer-col h4 { font-size: 9.5px; font-weight: 600; margin-bottom: 6px; }
  .footer-col p { font-size: 7.5px; line-height: 16px; color: var(--footer-muted); }
  .footer-col.address { left: 198px; }
  .footer-col.address p { padding-left: 3px; }
  .footer-col.phone { left: 413px; }
  .footer-col.email { left: 559px; }
  .social { position: absolute; top: 96px; left: 738px; display: flex; gap: 16px; }
  .social span { width: 9px; height: 9px; border-radius: 50%; background: #8a8a8a; }
  .social span.is-bright { background: var(--white); }
  .copyright { position: absolute; top: 160px; width: 100%; text-align: center; font-size: 7.5px; color: #6f6f6f; }
  .copyright strong { color: #a0a0a0; font-weight: 600; }
</style>
</head>
<body>
  <header class="site-header">
    <div class="brand">BRAMBLE RIDGE FOOT CARE</div>
    <nav class="main-nav">
      <a class="is-active" style="left:460px">Home</a>
      <a style="left:503px">About</a>
      <a style="left:550px">Podiatry Treatments</a>
      <a style="left:655px">Podiatry Products &amp; Footwear</a>
      <a style="left:803px">Health &amp; Wellness Products</a>
      <a style="left:939px">Links</a>
    </nav>
  </header>

  <section class="hero" role="img" aria-label="Photo placeholder: a person in flip-flops standing on a sandy beach facing the sea">
    <div class="hero-copy hero-address">Suite 12 / 75 Harwood Lane Melbourne 3000</div>
    <div class="hero-copy hero-phone">Phone 1300 555 014</div>
    <div class="hero-copy hero-email">info@brambleridgefootcare.com</div>
    <div class="btn btn-solid">Read More</div>
    <div class="btn btn-outline">Contact Now</div>
    <div class="slider-arrow prev"><svg width="6" height="8" viewBox="0 0 6 8"><path d="M4 1 L1.5 4 L4 7" fill="none" stroke="#fff" stroke-width="1"/></svg></div>
    <div class="slider-arrow next"><svg width="6" height="8" viewBox="0 0 6 8"><path d="M2 1 L4.5 4 L2 7" fill="none" stroke="#fff" stroke-width="1"/></svg></div>
    <div class="slider-dots"><span></span><span class="is-current"></span><span></span><span></span></div>
  </section>

  <section class="intro">
    <p>Bramble Ridge Foot Care is a Podiatry clinic in the heart of Melbourne CBD. We are located between Ash &amp; Elm Streets in the Harbourview Business Centre / Linden Hotel Complex.</p>
    <p>Our podiatrists are fully qualified health professionals who are able to diagnose, treat, manage or help to prevent all medical conditions that affect the feet and lower limb.</p>
    <p>We provide General Podiatry Treatment and some Specialised Services in relation to various foot conditions, including Sports Injuries, Orthotic Therapy and Nail Surgery.</p>
  </section>
  <div class="cta-bar cta-call">For Appointments or Enquiries please call us on 1300 555 014</div>
  <div class="cta-bar cta-mail">or email:&nbsp; info@brambleridgefootcare.com</div>

  <section class="promo-band">
    <div class="promo-title">Health &amp; Wellness Products&nbsp; At Bramble Ridge Foot Care</div>
    <div class="promo-text">we believe that maintaining a healthy &amp; active lifestyle is the best way to prevent or manage debilitating foot conditions.</div>
    <div class="btn btn-outline">Read More</div>
  </section>

  <footer class="site-footer">
    <div class="footer-brand">BRAMBLE RIDGE FOOT CARE</div>
    <div class="footer-col address">
      <h4>Postal Address</h4>
      <p>Suite 12 / 75 Harwood Lane<br>Melbourne 3000</p>
    </div>
    <div class="footer-col phone">
      <h4>Phone</h4>
      <p>1300 555 014</p>
    </div>
    <div class="footer-col email">
      <h4>Email</h4>
      <p>info@brambleridgefootcare.com</p>
    </div>
    <div class="social"><span></span><span class="is-bright"></span><span></span></div>
    <div class="copyright">© 2016 All Rights Reserved <strong>Bramble Ridge Foot Care</strong></div>
  </footer>
</body>
</html>
```